Killer Webpage Design

I currently have a self-hosted webpage through wordpress at www.varnetpixel.com - the content is complete and I'm happy with this but I need it designed (no coding) to complete my requirements. I'm happy to take designs which are non-Wordpress if there is specific advantage in this.

My full branding logos are attached along with color files. My main aim is consistent branding across all areas (social media, business cards, emails, websites). I have the rest running but am not happy with the available default selections from Wordpress.

I would prefer to use the darker blue version of the logo as I feel this has more standout in online media, however I would appreciate submissions with both variants to help me choose.

With the homepage I will also want to see blog pages and category pages designed but this can come after I have selected a design to go with,

Sites that I like and are related to my business include the following:
http://www.plumtally.com/au/accounting-software/
http://www.taskbrindle.com/home.aspx
https://tillnorth.com/register
Updates

Apologies for the confusion - to clarify for designers I am looking for design only, no coding.

FYI - i have now uploaded business cards for an idea of the contemporary style of design completed so far.

Target Market(s)

small to medium business. Not systemised but looking for help and support.

Industry/Entity Type

Business

Requirements
Must have
• I'm looking for a minimalist professional page, with the ability to easily add new sections when required. I will also need a CMS to add blog posts on the go, with the same features that it currently has (comments, social logon etc)

```html
<!DOCTYPE html>
<html lang="en">
<head>
<meta charset="utf-8">
<title>Varnet Pixel</title>
<link rel="stylesheet" href="https://fonts.googleapis.com/css2?family=Source+Sans+3:wght@400;600;700&display=swap">
<style>
:root{
  --red:#b01c22;
  --red-dark:#8e1218;
  --orange:#e0701f;
  --orange-dark:#c4561a;
  --teal:#5fb9c6;
  --teal-dark:#47a7b6;
  --blue:#1f5a7c;
  --text:#3a3a3a;
  --muted:#666;
  --light:#f2f2f2;
  --band:#e6e6e6;
  --footer:#2d2d2d;
  --white:#fff;
}
*{box-sizing:border-box;margin:0;padding:0}
html,body{width:908px;height:1200px;overflow:hidden}
body{font-family:"Source Sans 3",Arial,sans-serif;color:var(--text);background:var(--white);position:relative}
.wrap{position:absolute;left:69px;width:772px}

.site-header{position:absolute;top:0;left:0;width:908px;height:90px;background:linear-gradient(#fff,#f3f3f3)}
.brand{position:absolute;left:70px;top:28px;display:flex;align-items:center;gap:8px;font-size:25px;font-weight:600;color:var(--blue)}
.brand-dot{width:30px;height:30px;border-radius:50%;background:var(--orange)}
.search{position:absolute;left:610px;top:34px;width:160px;height:22px;border:1px solid #ccc;background:#fff;font-size:10px;color:#666;padding:4px 12px}
.search svg{position:absolute;right:6px;top:4px}
.lang{position:absolute;left:776px;top:34px;width:65px;height:22px;border:1px solid #ccc;background:#fff;font-size:10px;color:#666;padding:4px 0 0 24px}
.lang .flag{position:absolute;left:7px;top:7px;width:12px;height:8px;background:#2b4f8c;border:1px solid #c33}
.lang .caret{position:absolute;right:8px;top:9px;border:4px solid transparent;border-top-color:#555}

.main-nav{position:absolute;top:90px;left:0;width:908px;height:40px;background:linear-gradient(var(--red),var(--red-dark));box-shadow:0 3px 6px rgba(0,0,0,.3);z-index:2}
.main-nav ul{list-style:none;display:flex;position:absolute;left:69px;height:40px;border-right:1px solid #6e0c10}
.main-nav li{height:40px;line-height:40px;padding:0 11.5px;color:#fff;font-size:12.5px;border-left:1px solid #6e0c10}
.main-nav li.active{background:linear-gradient(#ec8a3c,var(--orange-dark));padding:0 12px}

.hero{position:absolute;top:130px;left:0;width:908px;height:240px;background:linear-gradient(#74c2cd,var(--teal-dark))}
.hero-art{position:absolute;left:90px;top:40px;width:315px;height:175px;border-radius:60px 60px 10px 10px;background:radial-gradient(ellipse at 40% 45%,#fafafa,#d9dde0 60%,rgba(200,210,215,0) 75%)}
.hero-copy{position:absolute;left:437px;top:36px;width:405px;color:#fff}
.hero-copy h1{font-size:18.5px;font-weight:700;line-height:27px}
.hero-copy p{font-size:11.5px;line-height:18px;margin-top:10px}
.btn-demo{display:inline-flex;align-items:center;gap:8px;margin-top:14px;height:35px;padding:0 10px;background:#fff;border-radius:3px;box-shadow:0 1px 3px rgba(0,0,0,.3);color:#333;font-size:16px}
.btn-demo b{font-weight:700}
.btn-demo i{width:17px;height:17px;border-radius:50%;background:#666;display:inline-flex;align-items:center;justify-content:center}

.welcome{position:absolute;top:370px;left:0;width:908px;height:535px;background:linear-gradient(#ececec,#fff 120px)}
h2.section-title{font-size:18.5px;font-weight:600;color:var(--red);line-height:22px}
.copy{font-size:11.6px;line-height:17.5px;color:var(--text)}
.btn{display:inline-block;height:30px;line-height:30px;padding:0 11px;border-radius:2px;background:linear-gradient(#ec8a3c,var(--orange-dark));color:#fff;font-size:12px;font-weight:600;box-shadow:0 1px 2px rgba(0,0,0,.3)}
.video{position:absolute;left:599px;top:60px;width:241px;height:151px;border-radius:3px;background:radial-gradient(circle at 60% 40%,#4a6a86,#1b2a3c 75%)}
.video svg{position:absolute;left:92px;top:48px}
.divider{position:absolute;top:244px;left:69px;width:772px;border-top:1px solid #ccc}

.service-col{position:absolute;top:270px;width:241px;height:240px}
.service-col .copy{text-align:justify;margin-top:16px}
.service-col .btn{position:absolute;top:204px;left:0}
.accordion{list-style:none;margin-top:18px}
.accordion li{height:34px;margin-bottom:1.5px;border:1px solid #d8d8d8;background:linear-gradient(#f4f4f4,#e7e7e7);display:flex;align-items:center;padding-left:15px;gap:13px;font-size:14px;font-weight:600;color:var(--blue)}
.accordion .arrow{width:16px;height:16px;border:1px solid #ccc;background:#fff;display:flex;align-items:center;justify-content:center}

.blog-band{position:absolute;top:905px;left:0;width:908px;height:209px;background:var(--band)}
.blog-nav{position:absolute;left:817px;top:18px}
.blog-image{position:absolute;left:69px;top:52px;width:241px;height:136px;border-radius:3px;background:radial-gradient(circle at 55% 40%,#3d7be0,#0b1f6e 70%)}
.blog-post{position:absolute;left:335px;top:55px;width:506px}
.blog-post h3{font-size:14px;font-weight:400;color:var(--blue)}
.blog-post .meta{font-size:9.5px;color:#333;margin-top:3px}
.blog-post .copy{text-align:justify;margin-top:10px}
.share{display:flex;gap:6px;margin-top:10px;font-size:8.5px}
.share span{border:1px solid #bbb;background:#fff;padding:1px 4px;border-radius:2px}
.share .gap{margin-left:6px}

.site-footer{position:absolute;top:1114px;left:0;width:908px;height:86px;background:var(--footer);color:#ddd}
.footer-links{position:absolute;left:69px;top:23px;font-size:11px;display:flex;gap:10px}
.footer-links .sep{color:#888}
.copyright{position:absolute;left:69px;top:50px;font-size:11px}
.social{position:absolute;left:799px;top:36px;display:flex;gap:6px}
.social span{width:18px;height:18px;border-radius:3px}
.social .one{background:#3b5998}.social .two{background:#4ab3e6}
</style>
</head>
<body>

<header class="site-header">
  <div class="brand"><span class="brand-dot"></span>Varnet Pixel</div>
  <div class="search">Search
    <svg width="12" height="12" viewBox="0 0 12 12"><circle cx="5" cy="5" r="3.5" fill="none" stroke="#222" stroke-width="2"/><line x1="7.5" y1="7.5" x2="11" y2="11" stroke="#222" stroke-width="2.4"/></svg>
  </div>
  <div class="lang"><span class="flag"></span>Eng<span class="caret"></span></div>
</header>

<nav class="main-nav">
  <ul>
    <li class="active">Home</li>
    <li>Software Training and Implementation</li>
    <li>Project Management</li>
    <li>Business Process Analysis</li>
    <li>Blog</li>
    <li>About Us</li>
    <li>Contact Us</li>
  </ul>
</nav>

<section class="hero">
  <div class="hero-art" role="img" aria-label="Illustration of a white cloud beside a rising bar chart"></div>
  <div class="hero-copy">
    <h1>Curabitur non massa vestibulum, egestas velit vitae, imperdiet velit.</h1>
    <p>Aliquam interdum sollicitudin odio. Mauris nunc ante, sagittis id porta quis, semper non neque. Suspendisse ac pulvinar tellus.</p>
    <span class="btn-demo"><b>FREE</b> Demo <i><svg width="8" height="8" viewBox="0 0 8 8"><path d="M2.5 1l3 3-3 3" fill="none" stroke="#fff" stroke-width="1.6"/></svg></i></span>
  </div>
</section>

<section class="welcome">
  <div class="wrap" style="top:27px">
    <h2 class="section-title">Welcome to Varnet Pixel</h2>
    <div style="width:504px;margin-top:13px">
      <p class="copy">Cloud computing spending is due to account for a third of annual IT expenditure growth by the end of 2013. Every year the range of cloud software systems gets bigger, now including Plum Tally Accounting, Gridwell Apps for Business, Jobsmith Job Management Software, Deskward Suite, Crewlink Project Manager and many more.</p>
      <p class="copy" style="margin-top:6px">Signing up for cloud software is only the first part of the process, and then it has to be implemented into your business. That's where Varnet Pixel comes in.</p>
      <span class="btn" style="margin-top:16px">VIEW MORE</span>
    </div>
  </div>
  <div class="video" role="img" aria-label="Video still of an open hand beneath a cloud">
    <svg width="56" height="56" viewBox="0 0 56 56"><circle cx="28" cy="28" r="25" fill="none" stroke="#fff" stroke-width="4"/><path d="M22 16l18 12-18 12z" fill="#fff"/></svg>
  </div>
  <div class="divider"></div>

  <div class="service-col" style="left:69px">
    <h2 class="section-title">Project Management</h2>
    <p class="copy">Project Management is one of the most important areas of any business operations, however can often be overlooked. Varnet Pixel can be engaged to help where project management is required but the resources are not available internally. Available for anything from half day reviews to several month projects, Varnet Pixel can be used as an outsourced resource to take out the pain of your project.</p>
    <span class="btn">CONTACT US</span>
  </div>
  <div class="service-col" style="left:335px">
    <h2 class="section-title">Business Process Analysis</h2>
    <p class="copy">Too often, small businesses spend plenty of time reviewing their market, and analysing competitior behaviour, but without ever taking a look inside their own operations. Varnet Pixel have experience with business reviews, marketing development, profit and loss analysis and much more, and can be engaged on anything from a half day review meeting to several months.</p>
    <span class="btn">CONTACT US</span>
  </div>
  <div class="service-col" style="left:599px">
    <h2 class="section-title" style="color:var(--orange-dark)">Software Training and Implementation</h2>
    <ul class="accordion">
      <li><span class="arrow"><svg width="6" height="8" viewBox="0 0 6 8"><path d="M1 1l3 3-3 3" fill="none" stroke="#555" stroke-width="1.3"/></svg></span>Plum Tally</li>
      <li><span class="arrow"><svg width="6" height="8" viewBox="0 0 6 8"><path d="M1 1l3 3-3 3" fill="none" stroke="#555" stroke-width="1.3"/></svg></span>Fieldhop</li>
      <li><span class="arrow"><svg width="6" height="8" viewBox="0 0 6 8"><path d="M1 1l3 3-3 3" fill="none" stroke="#555" stroke-width="1.3"/></svg></span>Gridwell Apps</li>
      <li><span class="arrow"><svg width="6" height="8" viewBox="0 0 6 8"><path d="M1 1l3 3-3 3" fill="none" stroke="#555" stroke-width="1.3"/></svg></span>Stockline</li>
      <li><span class="arrow"><svg width="6" height="8" viewBox="0 0 6 8"><path d="M1 1l3 3-3 3" fill="none" stroke="#555" stroke-width="1.3"/></svg></span>Cartsy</li>
    </ul>
  </div>
</section>

<section class="blog-band">
  <h2 class="section-title" style="position:absolute;left:69px;top:14px">Blog</h2>
  <svg class="blog-nav" width="24" height="14" viewBox="0 0 24 14"><path d="M8 2L3 7l5 5M16 2l5 5-5 5" fill="none" stroke="#444" stroke-width="2.4"/></svg>
  <div class="blog-image" role="img" aria-label="Glowing blue cloud above a circuit-board world map"></div>
  <article class="blog-post">
    <h3>Atullam volutpat dui et nisl pharetra, in convallis ipsum</h3>
    <p class="meta">July-31-13 &nbsp;:: &nbsp;10.15 a.m</p>
    <p class="copy">Pellentesque at tristique nunc. Nunc quam orci, egestas et tortor et, molestie adipiscing velit. Nunc hendrerit risus ut dui condimentum dignissim. Sed nec mattis augue. Nunc ante eros, eleifend ac odio id, dictum sagittis urna. Praesent eros dolor, condimentum ac laoreet id, laoreet vel sapien. Duis laoreet ac turpis eu molestie. Fusce facilisis nunc at orci congue aliquet.</p>
    <div class="share"><span>Like</span><span>3k</span><span class="gap">Post</span><span>316</span></div>
  </article>
</section>

<footer class="site-footer">
  <div class="footer-links">
    <span>Home</span><span class="sep">|</span><span>Software Training and Implementation</span><span class="sep">|</span><span>Project Management</span><span class="sep">|</span><span>Business Process Analysis</span><span class="sep">|</span><span>Blog</span><span class="sep">|</span><span>About Us</span><span class="sep">|</span><span>Contact Us</span>
  </div>
  <p class="copyright">Copyright &nbsp;© &nbsp;2013 &nbsp;&nbsp;Varnet Pixel. &nbsp;&nbsp;&nbsp;All rights reserved.</p>
  <div class="social"><span class="one"></span><span class="two"></span></div>
</footer>

</body>
</html>
```